Junior tennis development pathway graphic

The National Racquet Guild Assn.(NRGA) and the Global Court Sports Union (GCSU)
recommend (read demand) that all junior tennis programs now be ran using a progressive format of 4 different colored balls, different court sizes and scoring systems for various ages. We want to create a graphic for our juniors page on our web site that will show parents in a VERY EASY to understand way how their kids will progress through the various stages of tennis. The page is being built using Bootstrap and we plan to use jQuerry Hotspot to give detailed information over certain areas of the graphic. This specific information will be Dbase driven with class names,and specific class info. - The design does not need to show this, I just though it might be helpful to know
Updates

There are 2 other sites that will be helpful in understanding this project:

The first is www.smallcourtstarters.example and the second is my junior page on my current website
www.pinecrestracquetclub.example/juniora.cfm

I added a new file named jr pathway 2

This is an idea i had for the project - needs to be completed and given some sizzle

Target Market(s)

Parents of children ages 3-16

Industry/Entity Type

Progressive

Requirements
Must have
• Vector format
800x800 pixels max
EASY TO UNDERSTAND
Use of some or all of the key words and phrases in the uploaded file "keywords"
Should not have
• I do not want it to look like every other development graphic already out there.
To see what is currently being used image search
"tennis pathway" or "junior tennis pathway"

"pathway and" juniorspathway" in the uploaded files section are 2 ideas of VERY bad attempts

```html
<!DOCTYPE html>
<html lang="en">
<head>
<meta charset="utf-8">
<title>Four Stage Court Path – Junior Pathway</title>
<link rel="stylesheet" href="https://fonts.googleapis.com/css2?family=Open+Sans:wght@400;600;700;800&family=Noto+Serif:wght@400;700&display=swap">
<style>
  :root{
    --bg-light:#62c2bb;
    --bg-dark:#0a2624;
    --header:#0f4d46;
    --label-black:#121212;
    --red:#e3141e;
    --red-cell:#ee3a3a;
    --red-cell-2:#ff8a8a;
    --red-panel:#ff6a6a;
    --orange:#ec6a0c;
    --orange-cell:#f7a36b;
    --orange-cell-2:#fbb98a;
    --orange-panel:#ffb47f;
    --green:#168a2c;
    --green-cell:#2fae52;
    --green-cell-2:#43c168;
    --green-cell-3:#7ee3a0;
    --green-panel:#21a84a;
    --green-arrow:#45e03a;
    --yellow:#f5e600;
    --yellow-cell:#fff35a;
    --yellow-label:#f2d800;
    --white:#ffffff;
    --note-orange:#ff8a1e;
    --note-yellow:#ffe44a;
    --ink:#1c1c1c;
  }
  html,body{margin:0;padding:0;overflow:hidden;background:var(--bg-dark);}
  .pathway-canvas{
    width:1200px;height:1200px;overflow:hidden;position:relative;
    background:linear-gradient(135deg,var(--bg-light) 0%,#2f7f79 45%,var(--bg-dark) 100%);
  }
  .pathway-canvas svg{display:block;width:1200px;height:1200px;}
  .label-text{font-family:"Open Sans",Arial,sans-serif;font-weight:800;fill:var(--white);font-size:14px;letter-spacing:.3px;text-anchor:middle;}
  .header-text{font-family:"Open Sans",Arial,sans-serif;font-weight:600;fill:var(--white);text-anchor:middle;}
  .brand-name{font-family:"Open Sans",Arial,sans-serif;font-weight:700;fill:var(--ink);font-size:38px;text-anchor:middle;}
  .tagline{font-family:"Noto Serif",Georgia,serif;font-weight:700;fill:var(--ink);font-size:15px;text-anchor:middle;}
  .court-text{font-family:"Open Sans",Arial,sans-serif;font-weight:600;fill:var(--white);font-size:11.5px;}
  .court-text.dark{fill:var(--ink);}
  .age-text{font-family:"Open Sans",Arial,sans-serif;font-weight:600;fill:var(--ink);font-size:11px;text-anchor:middle;}
  .note{font-family:"Noto Serif",Georgia,serif;font-size:19px;}
  .note-lead{fill:var(--note-orange);}
  .note-question{fill:var(--note-yellow);}
  .note-item{fill:var(--white);}
  .ring{fill:var(--label-black);}
</style>
</head>
<body>
<main class="pathway-canvas">
<svg viewBox="0 0 800 800" xmlns="http://www.w3.org/2000/svg" aria-labelledby="pathway-title">
  <title id="pathway-title">Four Stage Court Path – your child's path to success at every level</title>
  <defs>
    <radialGradient id="ball-red" cx="40%" cy="35%" r="65%"><stop offset="0" stop-color="#ff8070"/><stop offset="1" stop-color="#c4000a"/></radialGradient>
    <radialGradient id="ball-orange" cx="40%" cy="35%" r="65%"><stop offset="0" stop-color="#ffb466"/><stop offset="1" stop-color="#d85200"/></radialGradient>
    <radialGradient id="ball-green" cx="40%" cy="35%" r="65%"><stop offset="0" stop-color="#e4f26a"/><stop offset=".55" stop-color="#9cc814"/><stop offset="1" stop-color="#5a8c00"/></radialGradient>
    <radialGradient id="ball-yellow" cx="40%" cy="35%" r="65%"><stop offset="0" stop-color="#f4ff70"/><stop offset="1" stop-color="#92b400"/></radialGradient>
    <linearGradient id="arrow-red" x1="0" x2="1"><stop offset="0" stop-color="#b30000"/><stop offset="1" stop-color="#ff2a2a"/></linearGradient>
    <linearGradient id="arrow-orange" x1="0" x2="1"><stop offset="0" stop-color="#a84a10"/><stop offset="1" stop-color="#ff8a30"/></linearGradient>
    <linearGradient id="arrow-green" x1="0" x2="1"><stop offset="0" stop-color="#1f7a28"/><stop offset="1" stop-color="#5ee05a"/></linearGradient>
  </defs>

  <!-- Title band -->
  <g class="brand-title">
    <circle cx="178" cy="50" r="14" fill="var(--ink)"/>
    <text class="brand-name" x="412" y="63">Four Stage Court Path</text>
    <text class="tagline" x="400" y="91">"Your Child's path to success at every level"</text>
  </g>

  <!-- Header bars -->
  <rect class="header-bar" x="33" y="97" width="329" height="28" fill="var(--header)"/>
  <text class="header-text" x="197" y="118" font-size="18">Developmental Programs</text>
  <rect class="header-column" x="365" y="97" width="170" height="146" fill="var(--header)"/>
  <text class="header-text" x="450" y="213" font-size="17">Competitive</text>
  <text class="header-text" x="450" y="235" font-size="17">Programs</text>
  <rect class="header-bar" x="540" y="97" width="230" height="28" fill="var(--header)"/>

  <!-- Grid cells -->
  <g class="stage-cells">
    <rect x="33" y="128" width="155" height="134" fill="var(--red-cell)"/>
    <rect x="193" y="128" width="167" height="134" fill="var(--red-cell-2)"/>
    <rect x="33" y="267" width="155" height="125" fill="var(--orange-cell)"/>
    <rect x="193" y="267" width="167" height="125" fill="var(--orange-cell-2)"/>
    <rect x="365" y="267" width="170" height="125" fill="var(--orange-cell-2)"/>
    <rect x="33" y="397" width="155" height="165" fill="var(--green-cell)"/>
    <rect x="193" y="397" width="167" height="165" fill="var(--green-cell-2)"/>
    <rect x="365" y="397" width="170" height="165" fill="var(--green-cell-3)"/>
    <rect x="365" y="567" width="170" height="203" fill="var(--yellow-cell)"/>
  </g>

  <!-- Stage headings -->
  <rect x="53" y="130" width="109" height="21" fill="var(--label-black)"/>
  <text class="header-text" x="107" y="147" font-size="16">LEARN</text>
  <rect x="228" y="130" width="107" height="21" fill="var(--label-black)"/>
  <text class="header-text" x="281" y="147" font-size="16">PLAY</text>
  <rect x="400" y="245" width="108" height="22" fill="var(--label-black)"/>
  <text class="header-text" x="454" y="262" font-size="16">COMPETE</text>

  <!-- Court spec panels -->
  <g class="court-panel court-panel--red">
    <rect x="540" y="128" width="230" height="134" rx="4" fill="var(--red-panel)"/>
    <rect x="548" y="134" width="147" height="74" fill="#e02020" role="img" aria-label="Red ball court diagram, 36 by 18 feet"/>
    <rect x="706" y="138" width="59" height="20" fill="#ffc0c0"/>
    <text class="age-text" x="735" y="152">AGE 4-8</text>
    <text class="court-text" x="551" y="228">36' x 18'</text>
    <text class="court-text" x="551" y="243">Racquets 19" - 23"</text>
  </g>
  <g class="court-panel court-panel--orange">
    <rect x="540" y="267" width="230" height="131" rx="4" fill="var(--orange-panel)"/>
    <rect x="548" y="273" width="147" height="67" fill="#f06a10" role="img" aria-label="Orange ball court diagram, 60 feet long"/>
    <rect x="700" y="278" width="65" height="20" fill="#ffd8bb"/>
    <text class="age-text" x="732" y="292">AGE 7-10</text>
    <text class="court-text dark" x="551" y="362">60' x 21' Singles</text>
    <text class="court-text dark" x="551" y="377">60' x 27' Doubles</text>
    <text class="court-text dark" x="551" y="392">Racquets 23" - 25"</text>
  </g>
  <g class="court-panel court-panel--green">
    <rect x="540" y="407" width="230" height="155" rx="4" fill="var(--green-panel)"/>
    <rect x="548" y="413" width="147" height="75" fill="#179a3d" role="img" aria-label="Green ball full court diagram, 78 feet long"/>
    <rect x="697" y="418" width="68" height="20" fill="#b8f0c8"/>
    <text class="age-text" x="731" y="432">AGE 10-12</text>
    <text class="court-text" x="551" y="524">78' x 27' Singles</text>
    <text class="court-text" x="551" y="540">78' x 36' Doubles</text>
    <text class="court-text" x="551" y="556">Racquets 26" - 27"</text>
  </g>
  <g class="court-panel court-panel--yellow">
    <rect x="540" y="567" width="230" height="203" rx="4" fill="var(--yellow)"/>
    <rect x="697" y="573" width="68" height="21" fill="#b6f0a0"/>
    <text class="age-text" x="731" y="588">AGE 13 &amp; up</text>
    <text class="court-text dark" x="551" y="748">Racquet 27" (Adult)</text>
  </g>

  <!-- Flow arrows -->
  <g class="flow-arrows">
    <path d="M170 204h30v-10l18 18-18 18v-10h-30z" fill="url(#arrow-red)"/>
    <path d="M170 333h30v-10l18 18-18 18v-10h-30z" fill="url(#arrow-orange)"/>
    <path d="M340 333h30v-10l18 18-18 18v-10h-30z" fill="url(#arrow-orange)"/>
    <path d="M335 362l42 42-6 6 22 4-4-22-6 6-42-42z" fill="url(#arrow-orange)"/>
    <path d="M170 478h30v-10l18 18-18 18v-10h-30z" fill="url(#arrow-green)"/>
    <path d="M340 478h30v-10l18 18-18 18v-10h-30z" fill="url(#arrow-green)"/>
    <path d="M330 525l40 48-7 6 20 8-2-22-7 6-40-48z" fill="var(--green-arrow)"/>
    <path d="M535 652h30v-12l22 20-22 20v-12h-30z" fill="#2a2a2a"/>
    <path d="M107 268h12v8h7l-13 14-13-14h7z" fill="var(--red)"/>
    <path d="M279 268h12v8h7l-13 14-13-14h7z" fill="var(--red)"/>
    <path d="M107 399h12v8h7l-13 14-13-14h7z" fill="var(--orange)"/>
    <path d="M279 399h12v8h7l-13 14-13-14h7z" fill="var(--orange)"/>
    <path d="M449 399h12v8h7l-13 14-13-14h7z" fill="var(--orange)"/>
    <path d="M449 571h12v8h7l-13 14-13-14h7z" fill="var(--green)"/>
  </g>

  <!-- Stage balls -->
  <g class="stage-ball">
    <circle class="ring" cx="125" cy="207" r="55"/>
    <circle cx="125" cy="207" r="46" fill="url(#ball-red)" role="img" aria-label="Red 1 ball"/>
    <rect x="65" y="250" width="85" height="20" rx="2" fill="var(--red)"/>
    <text class="label-text" x="107" y="265">RED 1</text>
  </g>
  <g class="stage-ball">
    <circle class="ring" cx="285" cy="207" r="55"/>
    <circle cx="285" cy="207" r="46" fill="url(#ball-red)" role="img" aria-label="Red 2 ball"/>
    <rect x="237" y="250" width="85" height="20" rx="2" fill="var(--red)"/>
    <text class="label-text" x="279" y="265">RED 2</text>
  </g>
  <g class="stage-ball">
    <circle class="ring" cx="125" cy="334" r="55"/>
    <circle cx="125" cy="334" r="46" fill="url(#ball-orange)" role="img" aria-label="Orange 1 ball"/>
    <rect x="62" y="381" width="90" height="20" rx="2" fill="var(--orange)"/>
    <text class="label-text" x="107" y="396">ORANGE 1</text>
  </g>
  <g class="stage-ball">
    <circle class="ring" cx="285" cy="334" r="55"/>
    <circle cx="285" cy="334" r="46" fill="url(#ball-orange)" role="img" aria-label="Orange 2 ball"/>
    <rect x="233" y="381" width="90" height="20" rx="2" fill="var(--orange)"/>
    <text class="label-text" x="278" y="396">ORANGE 2</text>
  </g>
  <g class="stage-ball">
    <circle class="ring" cx="455" cy="334" r="55"/>
    <circle cx="455" cy="334" r="46" fill="url(#ball-orange)" role="img" aria-label="JLT Orange ball"/>
    <rect x="403" y="381" width="104" height="20" rx="2" fill="var(--orange)"/>
    <text class="label-text" x="455" y="396">JLT ORANGE</text>
  </g>
  <g class="stage-ball">
    <circle class="ring" cx="125" cy="492" r="62"/>
    <circle cx="125" cy="492" r="52" fill="url(#ball-green)" role="img" aria-label="Green 1 ball"/>
    <rect x="62" y="551" width="90" height="20" rx="2" fill="var(--green)"/>
    <text class="label-text" x="107" y="566">GREEN 1</text>
  </g>
  <g class="stage-ball">
    <circle class="ring" cx="285" cy="492" r="62"/>
    <circle cx="285" cy="492" r="52" fill="url(#ball-green)" role="img" aria-label="Green 2 ball"/>
    <rect x="233" y="551" width="90" height="20" rx="2" fill="var(--green)"/>
    <text class="label-text" x="278" y="566">GREEN 2</text>
  </g>
  <g class="stage-ball">
    <circle class="ring" cx="455" cy="492" r="62"/>
    <circle cx="455" cy="492" r="52" fill="url(#ball-green)" role="img" aria-label="JLT Green ball"/>
    <rect x="403" y="551" width="104" height="20" rx="2" fill="var(--green)"/>
    <text class="label-text" x="455" y="566">JLT GREEN</text>
  </g>
  <g class="stage-ball">
    <circle class="ring" cx="455" cy="668" r="88"/>
    <circle cx="455" cy="668" r="76" fill="url(#ball-yellow)" role="img" aria-label="JLT Yellow ball"/>
    <rect x="395" y="758" width="113" height="20" rx="2" fill="var(--yellow-label)"/>
    <text class="label-text" x="451" y="773">JLT YELLOW</text>
  </g>
  <g class="stage-ball">
    <circle class="ring" cx="668" cy="660" r="70"/>
    <circle cx="668" cy="660" r="60" fill="url(#ball-yellow)" role="img" aria-label="High school team ball"/>
    <rect x="602" y="755" width="132" height="35" rx="2" fill="var(--yellow-label)"/>
    <text class="label-text" x="668" y="770">HIGH SCHOOL</text>
    <text class="label-text" x="668" y="786">TEAM</text>
  </g>

  <!-- Program note -->
  <g class="program-note">
    <text class="note note-lead" x="33" y="617">Giving lessons is not a program</text>
    <text class="note note-question" x="33" y="643">What is a program?</text>
    <text class="note note-item" x="33" y="670">-  Teaching/Coaching</text>
    <text class="note note-item" x="33" y="697">-  Training/Practicing</text>
    <text class="note note-item" x="33" y="723">-  Competition</text>
    <text class="note note-item" x="33" y="750">-  Play</text>
    <text class="note note-item" x="33" y="777">-  Social</text>
  </g>
</svg>
</main>
</body>
</html>
```